Verpackungen für Kosmetikhersteller
Zielgruppe
DE:
Wir sind ein junges Unternehmen, welches Kosmetik auf Kokosnussölbasis herstellt. Als erstes Produkt möchten wir ein Mundziehöl in verschiedenen Geschmacksrichtungen auf den Markt bringen. Zielgruppe sind gesundheitsbewusste Konsumenten im mittleren bis höherem Einkommensbereich. Für das Mundziehöl suchen wir nun ein Verpackungsdesign. Das Öl wird in Stickpacks zu 10 ml im Grundformat 30x110mm abgepackt (Skizze mit genauen Abstandsangaben im Anhang). Beispiele eines Stickpacks sind im Anhang als Stickpack example und Stickpack example2 hochgeladen. Neben unserem Loge sollte eine Angabe über die Geschmacksrichtung ebenfalls Platz auf der Verpackung finden.
EN:
We are a young start up, producing cosmetics based on coconut oil. As a first product we want to introduce a mouth pulling oil into the market. The oil will be sold in different flavors. The targeted consumer is a health conscious young adult in the middle to upper income range. The product will be filled in stickpacks (30x110mm) a 10 ml per pack. An example of an stick pack you can see as stickpack_example and stickpack_example2. The exact format, with dimensions you can see in the attachment skizze_30x110. The stickpack should show a simple and modern design however reflecting a high quality product for the health conscious consumer. The content should be our logo, the name of the product 'mirovalle' a feature which shows the flavor and a symbol or other feature to show that the product is coconut based. The design should not be overloaded. Simplicity but high class design is desirable.
Flavors are:
Pfefferminze (pepermint)
Limette (lime)
Zitrone (lemon)
Orange (orange)
Melisse (melissa)
Melisse / Orange (melissa/orange)
Blutorange (blood orange)
Fenchel (fennel)
Vanille (vanilla)
Zimt (cinnamon)
Aufgabenstellung
Das Design des Stickpacks sollte den jungen, gesundheitsbewussten Konsumenten ansprechen. Es sollte schlicht und modern gestaltet sein wobei erkennbar werden muss, dass es sich um ein höherpreisiges Qualitätsprodukt handelt. Es sollte weiterhin bemerkbar sein, dass der Grundstoff Kokosöl ist. Über ein einzelnes Feature sollte weiterhin erkennbar sein, um welche Geschmacksrichtung es sich handelt. Es sollen folgende Geschmacksrichtungen angeboten werden:
Pfefferminze
Limette
Zitrone
Orange
Melisse
Melisse / Orange
Blutorange
Fenchel
Vanille
Zimt
Der Name des Produktes, 'Mirovalle' sollte auch auf dem Stickpack ersichtlich sein, muss aber nicht zwingend im Mittelpunkt der Verpackung stehen.
Das Design sollte harmonisch wirken und nicht allzu große farbliche Kontraste aufweisen. Bilder von Kokosnüssen oder Palmen sowie weißer Zähne können gern eingearbeitet werden.

```html
<!DOCTYPE html>
<html lang="de">
<head>
<meta charset="utf-8">
<title>Mirovalle Fenchel – Stickpack</title>
<link rel="stylesheet" href="https://fonts.googleapis.com/css2?family=Oswald:wght@500;700&display=swap">
<style>
  :root {
    --backdrop: #ebebeb;
    --pack-white: #fbfbfb;
    --pack-edge: #e4e4e4;
    --gold: #d8cd98;
    --gold-dark: #c4b87e;
    --gold-text: #d6c995;
    --green: #2f8a35;
    --tone-brown: #b98a62;
    --tone-cream: #eee6da;
    --tone-seed: #c9c5a0;
  }
  * { margin: 0; padding: 0; box-sizing: border-box; }
  html, body {
    width: 1200px;
    height: 2974px;
    overflow: hidden;
    background: var(--backdrop);
  }
  .canvas {
    position: relative;
    width: 1200px;
    height: 2974px;
  }
  .stickpack {
    position: absolute;
    left: 324px;
    top: 259px;
    width: 564px;
    height: 2453px;
    background: var(--pack-white);
    box-shadow: 0 0 0 1px var(--pack-edge);
  }
  .seal {
    position: absolute;
    left: 0;
    width: 100%;
    background: var(--gold);
  }
  .seal svg { display: block; width: 100%; height: 100%; }
  .seal--top { top: 0; height: 173px; }
  .seal--bottom { bottom: 0; height: 151px; }

  .brand {
    position: absolute;
    top: 370px;
    left: 0;
    width: 100%;
    display: flex;
    justify-content: center;
    align-items: center;
    gap: 16px;
  }
  .brand__dot {
    width: 30px;
    height: 30px;
    border-radius: 50%;
    background: var(--green);
  }
  .brand__name {
    font-family: "Oswald", sans-serif;
    font-weight: 700;
    font-size: 80px;
    line-height: 1;
    color: var(--green);
    letter-spacing: 1px;
  }

  .product {
    position: absolute;
    top: 1010px;
    left: 0;
    width: 100%;
    text-align: center;
    font-family: "Oswald", sans-serif;
  }
  .product__name {
    font-weight: 700;
    font-size: 70px;
    line-height: 1;
    letter-spacing: 2px;
    color: var(--green);
    text-transform: uppercase;
  }
  .product__flavor {
    margin-top: 26px;
    font-weight: 700;
    font-size: 128px;
    line-height: 1;
    letter-spacing: 4px;
    color: var(--gold-text);
    text-transform: uppercase;
  }

  .ingredients {
    position: absolute;
    top: 1409px;
    left: 31px;
    width: 490px;
    height: 396px;
    border-radius: 28px;
    background: linear-gradient(160deg, var(--tone-cream) 0%, var(--tone-brown) 55%, var(--tone-seed) 100%);
  }
</style>
</head>
<body>
<main class="canvas">
  <section class="stickpack">
    <div class="seal seal--top">
      <svg viewBox="0 0 564 173" preserveAspectRatio="none" aria-hidden="true">
        <g stroke="var(--gold-dark)" stroke-width="3" opacity="0.6">
          <line x1="0" y1="30" x2="564" y2="30"/>
          <line x1="0" y1="55" x2="564" y2="55"/>
          <line x1="0" y1="80" x2="564" y2="80"/>
          <line x1="0" y1="105" x2="564" y2="105"/>
          <line x1="0" y1="130" x2="564" y2="130"/>
        </g>
      </svg>
    </div>

    <div class="brand">
      <span class="brand__dot"></span>
      <span class="brand__name">kernbloom</span>
    </div>

    <div class="product">
      <p class="product__name">Mirovalle</p>
      <p class="product__flavor">Fenchel</p>
    </div>

    <div class="ingredients" role="img" aria-label="Foto einer aufgebrochenen Kokosnuss mit Palmblatt und einem Häufchen Fenchelsamen"></div>

    <div class="seal seal--bottom">
      <svg viewBox="0 0 564 151" preserveAspectRatio="none" aria-hidden="true">
        <g stroke="var(--gold-dark)" stroke-width="3" opacity="0.6">
          <line x1="0" y1="25" x2="564" y2="25"/>
          <line x1="0" y1="50" x2="564" y2="50"/>
          <line x1="0" y1="75" x2="564" y2="75"/>
          <line x1="0" y1="100" x2="564" y2="100"/>
          <line x1="0" y1="125" x2="564" y2="125"/>
        </g>
      </svg>
    </div>
  </section>
</main>
</body>
</html>
```